Booklet Design needed for Brightfold Web Studio

A Little bit about us:
At Brightfold Web Studio we offer our clients the very best in their website needs without the big price tag.

We take the hassle out of setting up a website and take care of the website design, domain registration, SEO and hosting.
We know how important it is to have a Visually Appealing website, that’s why when we are designing our websites we focus on the main things like branding, content, creativity, colors, layout, ease of use, and imagery.

Design Specifics:
I currently have two booklets that I give to my clients:
one before I start designing their site as a general information booklet
and the other one I give only once I complete their site - which is about how to use my editor.

I want to jazz these two booklets up and bit with a modern and professional look, and I want both the booklets to have a similar design, I would also like it to be a similar look to my website, www.brightfoldwebstudio.com.au.

Previously the budget was AUD$130. Now it is AUD$260.
This reflects your creative effort for 2 booklets.

I have uploaded the two booklets, labeled Booklet 1 (7 pages) and Booklet 2 (15 pages), inside you will find the information and images I want on each page.
The booklets also need a title page.

Thanks Designers. Will appreciate all your creative effort!

Hi Designers . i have updated the content for one of the booklets. the new file which i will upload shortly is called "New Client information Booklet content update". please use this for one of the booklets to be designed. the other booklet still needs to be done (the one with the editor information inside)Cheers Added Thursday, October 29, 2015

Target Market(s)

Small to medium Businesses

Font styles to use
Sans Serif

Colors
3176b5
5c5c5c
ffffff

Requirements
Must have
• Logo, images and content from original booklets. And the Seperate booklets for the two different booklets. Similar modern, professional design.
Nice to have
• Moder, professional design, similar look to my website. Www.brightfoldwebstudio.com.au

```html
<!DOCTYPE html>
<html lang="en">
<head>
<meta charset="UTF-8">
<title>Brightfold Web Studio – Corporate Brochure Cover</title>
<link href="https://fonts.googleapis.com/css2?family=Open+Sans:wght@400;600;700&display=swap" rel="stylesheet">
<style>
  :root {
    --brand-blue: #3176b5;
    --brand-grey: #5c5c5c;
    --paper: #ffffff;
    --backdrop: #e6e6e6;
    --photo-deep: #0f2a5c;
    --photo-mid: #2f62b0;
    --photo-light: #8fb4e6;
    --panel-tint: rgba(120, 170, 230, 0.55);
  }
  * { box-sizing: border-box; margin: 0; padding: 0; }
  html, body {
    width: 1200px;
    height: 800px;
    overflow: hidden;
    background: var(--backdrop);
    font-family: "Open Sans", Arial, sans-serif;
  }
  .canvas {
    position: relative;
    width: 1200px;
    height: 800px;
  }
  .cover {
    position: absolute;
    left: 338px;
    top: 30px;
    width: 524px;
    height: 740px;
    background: var(--paper);
    box-shadow: 0 10px 30px rgba(0, 0, 0, 0.18);
    overflow: hidden;
  }
  .cover-header {
    position: absolute;
    left: 0;
    top: 0;
    width: 100%;
    height: 150px;
  }
  .brand-name {
    position: absolute;
    left: 58px;
    top: 90px;
    display: flex;
    align-items: center;
    gap: 10px;
    font-size: 22px;
    font-weight: 700;
    color: var(--brand-grey);
    letter-spacing: 0.3px;
  }
  .brand-square {
    width: 14px;
    height: 14px;
    background: var(--brand-blue);
  }
  .cover-photo {
    position: absolute;
    left: 0;
    top: 150px;
    width: 100%;
    height: 460px;
    background:
      radial-gradient(ellipse at 78% 22%, var(--photo-light) 0%, rgba(143, 180, 230, 0) 45%),
      linear-gradient(200deg, var(--photo-mid) 0%, #1d4a94 55%, var(--photo-deep) 100%);
  }
  .title-panel {
    position: absolute;
    left: 72px;
    top: 108px;
    width: 226px;
    height: 222px;
    background: var(--panel-tint);
    display: flex;
    align-items: center;
    justify-content: center;
  }
  .title-frame {
    border: 1px solid rgba(255, 255, 255, 0.85);
    padding: 8px 12px 9px;
    color: var(--paper);
    font-size: 26px;
    font-weight: 600;
    line-height: 1.15;
    text-align: center;
    letter-spacing: 0.5px;
    text-transform: uppercase;
  }
  .cover-footer {
    position: absolute;
    left: 0;
    top: 610px;
    width: 100%;
    height: 130px;
  }
  .site-address {
    position: absolute;
    right: 40px;
    top: 26px;
    font-size: 10px;
    font-weight: 400;
    color: var(--brand-blue);
    text-transform: uppercase;
    letter-spacing: 0.4px;
  }
</style>
</head>
<body>
  <main class="canvas">
    <section class="cover">
      <header class="cover-header">
        <div class="brand-name">
          <span class="brand-square"></span>
          <span>Brightfold Web Studio</span>
        </div>
      </header>

      <div class="cover-photo" role="img" aria-label="Photo of a businessman's hand in a dark suit sleeve touching a glowing virtual screen button on a blue background">
        <div class="title-panel">
          <h1 class="title-frame">Corporate<br>Brochure</h1>
        </div>
      </div>

      <footer class="cover-footer">
        <p class="site-address">www.brightfoldwebstudio.com.au</p>
      </footer>
    </section>
  </main>
</body>
</html>
```